Health Coach needs a Business Card Design

Need a really modern feminine business card design for a health and lifestyle coach. Needs to use geometric shapes, muted grey/blue/green pastels and black and white - see mood board attached and logo. The client likes black and white, modern, san serif with the use of lines and possibly a shadow leaf as in the mood board. Possibly put the tag line on the back or an icon of the logo. Logo is also attached. An icon of the logo would be great too.

Target Market(s)

Women (some men) aged 30 to 50.

Industry/Entity Type

Business

Contact Information for Business Card

Marla Teveny
e-mail: hello@marlatwell.example
website: marlatwell.example
Phone: +610497258316

The tag line is "Calm strength every day"

Font styles to use
Sans Serif

Colors
ecf7fb
cfeae6
000000
ffffff
f5f5f5

Requirements
Must have
• Black and white, logo, tag line and details
Nice to have
• Would be nice to incorporate the shadow palm.fern leaves as in the mood board and or geometric lines/shapes - see mood board. Could be either standard rectangle or would be happy with square too.
Should not have
• Flowers or decorations

```html
<!DOCTYPE html>
<html lang="en">
<head>
<meta charset="utf-8">
<title>Teveny Well — Business Card</title>
<link rel="stylesheet" href="https://fonts.googleapis.com/css2?family=Jost:wght@300;400&display=swap">
<style>
  :root {
    --backdrop: #a39890;
    --card-black: #000000;
    --ink-white: #ffffff;
    --ink-grey: #bdbdbd;
    --divider: #6a6a6a;
    --band-mint: #dff5f2;
    --band-ink: #2a2a2a;
  }
  * { margin: 0; padding: 0; box-sizing: border-box; }
  html, body {
    width: 1200px; height: 864px; overflow: hidden;
    background: var(--backdrop);
    font-family: "Jost", sans-serif;
  }
  .stage {
    width: 1200px; height: 864px;
    display: flex; flex-direction: column;
    align-items: center; justify-content: center; gap: 44px;
  }
  .card {
    width: 640px; height: 366px;
    background: var(--card-black);
    position: relative; overflow: hidden;
  }

  /* Back side */
  .card--back {
    display: flex; flex-direction: column;
    align-items: center; justify-content: center; gap: 16px;
  }
  .brand-name {
    font-weight: 300; color: var(--ink-grey);
    font-size: 38px; letter-spacing: 0.04em; line-height: 1;
    white-space: nowrap;
  }
  .brand-tagline {
    font-weight: 300; color: var(--ink-grey);
    font-size: 13px; letter-spacing: 0.32em; text-transform: uppercase;
    white-space: nowrap;
  }

  /* Front side */
  .card--front { display: flex; flex-direction: column; }
  .front-main { flex: 1; display: flex; position: relative; }
  .front-brand {
    width: 50%; display: flex; flex-direction: column;
    align-items: center; justify-content: center; gap: 12px;
  }
  .front-brand .brand-name { font-size: 32px; }
  .front-brand .brand-tagline { font-size: 9px; letter-spacing: 0.28em; }
  .front-divider {
    position: absolute; left: 50%; top: 36px; bottom: 30px;
    width: 1px; background: linear-gradient(var(--divider), #2a2a2a);
  }
  .front-details {
    width: 50%; padding: 40px 30px 26px 20px;
    display: flex; flex-direction: column; align-items: flex-end;
    justify-content: space-between; color: var(--ink-white);
  }
  .person-name { font-weight: 300; font-size: 24px; white-space: nowrap; }
  .contact-list { list-style: none; display: flex; flex-direction: column; gap: 6px; }
  .contact-item {
    display: flex; align-items: center; justify-content: flex-end; gap: 12px;
    font-weight: 300; font-size: 15px; white-space: nowrap;
  }
  .contact-icon { width: 14px; height: 14px; fill: var(--ink-white); flex: none; }
  .tagline-band {
    height: 76px; background: var(--band-mint);
    display: flex; align-items: center; justify-content: center;
    color: var(--band-ink); font-weight: 400;
    font-size: 20px; letter-spacing: 0.42em; text-transform: uppercase;
    white-space: nowrap;
  }
</style>
</head>
<body>
<main class="stage">
  <section class="card card--back" aria-label="Card back">
    <div class="brand-name">Teveny Well</div>
    <div class="brand-tagline">Calm strength every day</div>
  </section>

  <section class="card card--front" aria-label="Card front">
    <div class="front-main">
      <div class="front-brand">
        <div class="brand-name">Teveny Well</div>
        <div class="brand-tagline">Calm strength every day</div>
      </div>
      <div class="front-divider"></div>
      <div class="front-details">
        <div class="person-name">Marla Teveny</div>
        <ul class="contact-list">
          <li class="contact-item">+610497258316
            <svg class="contact-icon" viewBox="0 0 16 16" aria-hidden="true"><path d="M4 1l2.5 3-1.5 1.6c.8 2 2.4 3.6 4.4 4.4L11 8.5l3 2.5-1.2 2.7C7 13.5 2.5 9 2.3 3.2z"/></svg>
          </li>
          <li class="contact-item">hello@marlatwell.example
            <svg class="contact-icon" viewBox="0 0 16 16" aria-hidden="true"><path d="M1 3h14v10H1z M2 4l6 5 6-5" fill="none" stroke="#fff" stroke-width="1.4"/></svg>
          </li>
          <li class="contact-item">marlatwell.example
            <svg class="contact-icon" viewBox="0 0 16 16" aria-hidden="true"><g fill="none" stroke="#fff" stroke-width="1.3"><circle cx="8" cy="8" r="6.5"/><ellipse cx="8" cy="8" rx="3" ry="6.5"/><path d="M1.5 8h13"/></g></svg>
          </li>
        </ul>
      </div>
    </div>
    <div class="tagline-band">Calm strength every day</div>
  </section>
</main>
</body>
</html>
```